Webdesign für IT Service Firma
Zielgruppe
Wir sind eine IT-Service Firma und bieten individuelle IT-Lösungen. Unsere Kunden sind KMU, also Firmen mit einer Grösse von 2-250 Mitarbeitern im Grossraum Basel, die in Ihrem Bereich Spezialisten sind und spezielle Anforderungen an Ihre IT besitzen.
Unsere USP sind fixe Ansprechpartner, gute Erreichbarkeit, schneller und individueller Service
Aufgabenstellung
Schriftart Myriad Pro
Grün: #7FA51D
Blau: #4D9BC2
Grau: #999999
Untertitel: Wir sind da.

```html
<!DOCTYPE html>
<html lang="de">
<head>
<meta charset="utf-8">
<title>Norvalis – Webdesign</title>
<link href="https://fonts.googleapis.com/css2?family=PT+Sans+Narrow:wght@400;700&family=Source+Sans+3:wght@400;600;700&display=swap" rel="stylesheet">
<style>
  :root{
    --green:#7FA51D;
    --blue:#4D9BC2;
    --teal:#1a8fb0;
    --grey:#999999;
    --text:#333;
    --panel:#f6f6f6;
    --stage:#a7c1d0;
  }
  *{box-sizing:border-box;margin:0;padding:0}
  html,body{width:1200px;height:720px;overflow:hidden}
  body{background:linear-gradient(180deg,#9fbccd 0%,#93b2c4 60%,#aac6d6 100%);font-family:"Source Sans 3",sans-serif;color:var(--text);position:relative}
  .page{position:absolute;top:130px;width:370px;height:460px;background:#fff;overflow:hidden;box-shadow:0 10px 30px rgba(40,70,90,.25)}
  .page--services{left:25px}
  .page--home{left:415px}
  .page--contact{left:805px}
  .narrow{font-family:"PT Sans Narrow",sans-serif}

  /* services */
  .services__wedge{position:absolute;left:0;top:0;width:100%;height:100%}
  .services__title{position:absolute;top:22px;left:110px;right:20px;text-align:center;color:var(--teal);font-weight:700;font-size:17px;line-height:1.3}
  .service{position:absolute;top:110px;width:112px}
  .service:nth-of-type(1){left:12px}
  .service:nth-of-type(2){left:132px}
  .service:nth-of-type(3){left:252px}
  .service__icon{display:block;margin:0 auto 4px;width:40px;height:46px}
  .service__name{text-align:center;color:var(--grey);font-size:11px;padding-bottom:4px;border-bottom:2px solid var(--green);margin-bottom:8px}
  .service__list{list-style:none;font-size:7.5px;line-height:1.75;color:#555}
  .service__list li::before{content:"o ";color:var(--blue)}

  /* home */
  .home__hero{position:absolute;left:0;top:0;width:100%;height:280px;background:radial-gradient(ellipse at 65% 35%,#6b6a62 0%,#3e4446 45%,#2a3238 100%)}
  .home__logo{position:absolute;top:26px;left:18px;display:flex;align-items:center;gap:6px;color:var(--blue);font-size:20px;font-weight:600;letter-spacing:.5px}
  .home__logo span.dot{width:9px;height:9px;background:var(--green);border-radius:50%}
  .home__menu{position:absolute;top:26px;right:18px;width:22px}
  .home__menu i{display:block;height:2px;background:var(--green);margin-bottom:4px}
  .home__headline{position:absolute;top:170px;left:18px;color:var(--green);font-size:26px;font-weight:700;letter-spacing:.5px}
  .home__lower{position:absolute;top:280px;left:0;width:100%;height:180px;background:linear-gradient(118deg,#dcdcdc 0%,#dcdcdc 55%,#fff 55%)}
  .home__sub{position:absolute;top:300px;left:0;width:300px;text-align:center;color:var(--teal);font-weight:700;font-size:22px}
  .home__intro{position:absolute;top:340px;left:20px;width:290px;text-align:center;font-size:14px;line-height:1.45}

  /* contact */
  .contact__hero{position:absolute;left:0;top:0;width:100%;height:140px;background:linear-gradient(100deg,#141a22 0%,#243241 45%,#8a7468 70%,#d9b8a2 100%)}
  .contact__claim{position:absolute;top:14px;left:0;right:0;text-align:center;color:var(--green);font-size:21px;font-weight:700;letter-spacing:.3px}
  .contact__title{position:absolute;top:160px;left:0;right:0;text-align:center;color:var(--green);font-size:14px;font-weight:700}
  .contact__text{position:absolute;top:182px;left:55px;right:55px;text-align:center;font-size:7.5px;line-height:1.6;color:#444}
  .contact__address{position:absolute;top:265px;left:40px;font-size:11px;line-height:1.5;color:var(--grey)}
  .contact__address h3{color:var(--green);font-size:13px;margin-bottom:14px}
  .contact__form{position:absolute;top:262px;left:200px;width:150px}
  .contact__field{display:block;height:18px;border:1px solid #888;background:#fff;font-size:7.5px;color:#777;padding:3px 4px;margin-bottom:12px}
</style>
</head>
<body>

<section class="page page--services">
  <svg class="services__wedge" viewBox="0 0 370 460" aria-hidden="true"><polygon points="0,0 120,0 0,170" fill="#dedede"/></svg>
  <h2 class="services__title narrow">Maßgeschneiderte Leistungen<br>für Ihr Unternehmen</h2>

  <div class="service">
    <svg class="service__icon" viewBox="0 0 40 46" fill="none" stroke="#1a8fb0" stroke-width="1.6"><rect x="2" y="4" width="36" height="26" rx="1"/><path d="M14 40h12M20 30v10"/><path d="M20 9l7 3v5c0 4-3 7-7 8-4-1-7-4-7-8v-5z"/><path d="M17 17l2 2 4-4"/></svg>
    <div class="service__name narrow">Support</div>
    <ul class="service__list">
      <li>Internetzugang installieren</li><li>Problembehebung Remote bei uns vor Ort</li><li>VPN / Remote-Zugriff</li><li>Viren-, Trojaner- und Malware-Entfernung</li><li>Drucker und Scanner</li><li>Systemoptimierung</li><li>Netzwerk und WLAN Konfiguration</li><li>Serverinstallation</li><li>Serverwartung</li><li>Sichere Backup-Lösungen</li>
    </ul>
  </div>
  <div class="service">
    <svg class="service__icon" viewBox="0 0 40 46" fill="none" stroke="#1a8fb0" stroke-width="1.6"><path d="M20 2l16 6v12c0 12-8 20-16 24C12 40 4 32 4 20V8z"/><rect x="14" y="21" width="12" height="10" rx="1"/><path d="M16 21v-4a4 4 0 018 0v4"/></svg>
    <div class="service__name narrow">Sicherheit</div>
    <ul class="service__list">
      <li>Verschlüsselung von Dateien, Containern und ganzen Festplatten</li><li>Konfiguration von Firewalls und Switches</li><li>VPN-Zugänge</li><li>Verschlüsselung von vertraulicher Kommunikation, bspw. via Mail</li><li>Verschlüsselung von Daten in der Cloud</li><li>Verschlüsselung der Internetverbindung</li>
    </ul>
  </div>
  <div class="service">
    <svg class="service__icon" viewBox="0 0 40 46" fill="none" stroke="#1a8fb0" stroke-width="1.6"><path d="M6 2h22v38H6z"/><path d="M11 10h12M11 16h12M11 22h8M11 28h6"/><circle cx="29" cy="33" r="8"/><path d="M25 33l3 3 5-5"/></svg>
    <div class="service__name narrow">Beratung</div>
    <ul class="service__list">
      <li>Herstellerunabhängige Kaufberatung</li><li>Infrastruktur- und Netzwerk-Planung</li><li>IT-Coaching für Anwender und Entscheider</li><li>IT Supervision für Ihre internen Techniker</li><li>IT-Prozessoptimierung</li><li>IT-Projektleitung für Unternehmen</li><li>Gestaltung von Backup Prozessen</li>
    </ul>
  </div>
</section>

<section class="page page--home">
  <div class="home__hero" role="img" aria-label="Foto: zwei Personen arbeiten gemeinsam an einem Bildschirm im Büro"></div>
  <div class="home__logo"><span class="dot"></span>NORVALIS</div>
  <div class="home__menu"><i></i><i></i><i></i></div>
  <h1 class="home__headline narrow">WIR KÜMMERN UNS UM IHRE IT</h1>
  <div class="home__lower"></div>
  <h2 class="home__sub narrow">Wir sind da!</h2>
  <p class="home__intro">Norvalis GmbH ist Ihr Partner für IT Dienstleistungen. Wir entwickeln Lösungen für Ihr Unternehmen.</p>
</section>

<section class="page page--contact">
  <div class="contact__hero" role="img" aria-label="Bild: Finger berührt eine leuchtende digitale Oberfläche"></div>
  <h1 class="contact__claim narrow">TECHNOLOGY FOR THE NEXT GENERATION</h1>
  <h2 class="contact__title narrow">Wir freuen uns über Ihre Kontaktaufnahme!</h2>
  <p class="contact__text">Stet clita kasd gubergren, no sea takimata sanctus est Lorem ipsum dolor sit amet. Lorem ipsum dolor sit amet, consetetur sadipscing elitr, sed diam nonumy eirmod tempor invidunt ut labore et dolore magna aliquyam erat, sed diam voluptua. At vero eos et accusam et justo duo dolores et ea rebum. Stet clita kasd gubergren, no sea takimata sanctus est Lorem ipsum dolor sit amet.</p>
  <address class="contact__address narrow" style="font-style:normal">
    <h3>Unsere Büroadresse</h3>
    Norvalis GmbH<br>Lindenweg 14<br>CH-4000 Musterstadt<br><br>E-Mail: support@norvalis.ch
  </address>
  <form class="contact__form">
    <span class="contact__field">Name</span>
    <span class="contact__field">E-Mail</span>
    <span class="contact__field">Telefonnummer</span>
  </form>
</section>

</body>
</html>
```